Quillmark Letterpress Printing needs a "poster" for Vending Machine to sell mini-letterp...

I am a letterpress printer and have just purchased a small vending machine to take to craft markets/local boutiques and sell Mini-Letterpress Prints for $1 (four quarters).  Here is a link to what the machine looks like:  https://www.treatvendco.example/Heron-Decal-and-Stamp-Vending-Unit-Q4817.aspx
I need you all to design fun artwork for the front of the machine... dimensions are:  18" height, 15" width.  My company website is Quillmarkletterpress.example if you want to see my branding.  The mini-prints will constantly be changing, and each will be signed (by me).  I would like a strong "letterpress" look.... old school Brindle Yard Press type vibe.  I want it to look fun, colorful, and capture many impulse purchases.

Target Market(s)
impulse purchasers at artisan craft markets and small high end boutique stores
Requirements
Must have
- would prefer the colors to coordinate and/or mostly match my brand

Nice to have
- I would like to have a manicule on the design.... maybe: 4 quarters [manicule] 1 surprise print

Should not have
- comic sans

```html
<!DOCTYPE html>
<html lang="en">
<head>
<meta charset="utf-8">
<title>Quillmark Letterpress – Vending Machine Poster</title>
<link rel="stylesheet" href="https://fonts.googleapis.com/css2?family=Bebas+Neue&family=Ultra&display=swap">
<style>
  :root {
    --maroon: #941b4e;
    --olive: #8c9a2e;
    --cream: #fbf6e6;
    --tan: #f1dca4;
    --stage: #6b6b6b;
  }
  html, body {
    margin: 0;
    width: 1200px;
    height: 1117px;
    overflow: hidden;
    background: var(--stage);
  }
  .poster {
    position: absolute;
    left: 158px;
    top: 28px;
    width: 1113px;
    height: 1335px;
    background: var(--cream);
    transform: scale(0.794);
    transform-origin: top left;
    overflow: hidden;
  }
  .poster-art {
    position: absolute;
    inset: 0;
  }
  .poster > .text {
    position: absolute;
    margin: 0;
    line-height: 1;
    white-space: nowrap;
  }
  .brand-mark {
    left: 449px;
    top: 196px;
    width: 213px;
    text-align: center;
    font-family: "Bebas Neue", sans-serif;
    font-size: 92px;
    line-height: 0.9 !important;
    color: var(--maroon);
  }
  .title-the {
    left: 166px;
    top: 604px;
    font-family: "Bebas Neue", sans-serif;
    font-size: 64px;
    font-weight: 400;
    color: var(--olive);
  }
  .title-word {
    left: 257px;
    top: 450px;
    width: 740px;
    font-family: "Bebas Neue", sans-serif;
    font-size: 280px;
    color: var(--olive);
    transform: scaleX(0.82);
    transform-origin: left top;
    text-shadow: 3px 3px 0 rgba(90, 100, 20, 0.35);
  }
  .title-letterpress {
    left: 92px;
    top: 676px;
    font-family: "Bebas Neue", sans-serif;
    font-size: 302px;
    color: var(--maroon);
    transform: scaleX(0.757);
    transform-origin: left top;
    text-shadow: 3px 3px 0 rgba(80, 10, 40, 0.35);
  }
  .stars {
    top: 956px;
    font-size: 46px;
    letter-spacing: 14px;
    color: var(--olive);
  }
  .stars-left { left: 100px; }
  .stars-right { left: 858px; }
  .studio-name {
    left: 280px;
    width: 553px;
    top: 950px;
    text-align: center;
    font-family: "Ultra", serif;
    font-size: 56px;
    color: var(--olive);
  }
  .address {
    left: 93px;
    top: 1037px;
    width: 929px;
    height: 122px;
    background: var(--maroon);
    color: var(--cream);
    font-family: "Ultra", serif;
    font-size: 44px;
    letter-spacing: 3px;
    text-align: center;
    font-style: normal;
    display: flex;
    flex-direction: column;
    justify-content: center;
    gap: 4px;
  }
  .email {
    left: 93px;
    width: 929px;
    top: 1190px;
    text-align: center;
    font-family: "Ultra", serif;
    font-size: 30px;
    letter-spacing: 14px;
    color: var(--maroon);
  }
</style>
</head>
<body>
  <main class="poster">
    <svg class="poster-art" viewBox="0 0 1113 1335" width="1113" height="1335">
      <defs>
        <clipPath id="band-clip">
          <rect x="42" y="42" width="1028" height="340"/>
        </clipPath>
        <clipPath id="rays-clip">
          <rect x="0" y="0" width="1113" height="582"/>
        </clipPath>
        <radialGradient id="rays-fill" cx="50%" cy="100%" r="100%">
          <stop offset="0" stop-color="#f8ecc8"/>
          <stop offset="1" stop-color="#f1dca4"/>
        </radialGradient>
      </defs>

      <rect class="frame-line" x="20" y="18" width="1073" height="1297" fill="none" stroke="var(--maroon)" stroke-width="3"/>

      <g clip-path="url(#rays-clip)" role="img" aria-label="Sunburst rays radiating behind the title">
        <ellipse cx="557" cy="582" rx="460" ry="460" fill="url(#rays-fill)" opacity="0.85"/>
      </g>

      <g clip-path="url(#band-clip)">
        <path class="top-band" fill-rule="evenodd" fill="var(--maroon)"
          d="M42 42 H1070 V382 H42 Z M112 400 A445 300 0 0 1 1002 400 Z"/>
        <ellipse class="dashed-arc" cx="557" cy="400" rx="475" ry="310" fill="none"
          stroke="var(--cream)" stroke-width="6" stroke-dasharray="30 16"/>
      </g>
      <line x1="42" y1="372" x2="85" y2="372" stroke="var(--cream)" stroke-width="6" stroke-dasharray="20 12"/>
      <line x1="1030" y1="372" x2="1070" y2="372" stroke="var(--cream)" stroke-width="6" stroke-dasharray="20 12"/>

      <rect class="rule-bottom" x="93" y="1240" width="929" height="8" fill="var(--maroon)"/>
    </svg>

    <p class="text brand-mark">QUILL<br>MARK</p>

    <h1 class="text title-the">THE</h1>
    <p class="text title-word">INKWELL</p>
    <p class="text title-letterpress">LETTERPRESS</p>

    <p class="text stars stars-left">★★★</p>
    <p class="text studio-name">QUILLMARK</p>
    <p class="text stars stars-right">★★★</p>

    <address class="text address">
      <span>48 LARKSPUR LANE</span>
      <span>FAIRHAVEN, OR 97450</span>
    </address>

    <p class="text email">HELLO@QUILLMARK.EXAMPLE</p>
  </main>
</body>
</html>
```